素人ながらに一応簡単に自分で作成しました

今回はコロナの為、葬儀を簡潔に済ませる方が増えてきており(蜜を避ける)
火葬式メインのチラシを考えております。
とはいえ、家族葬と比較しているお客様にも他のプランもあることを
告知はしたいと思います。
(コロナ対策として、検温実施・お席の間隔を空ける・アルコール除菌・受付所の飛沫感染ボード用意等)

内容(項目や金額)を参考にしていただきレイアウトや色使いその他画像
をデザイナーさん目線でお願いいたします。

皆様の提案を見て、更ににあれこれ入れてほしいと要望が出るかもしれませんがよろしくお願いいたします。

記載項目
【社名】アオイ葬祭
【住所】さいたま市緑区上小池412-5
【電話】フリーダイヤル 0120-53-1046
【ロゴ】添付いたします
【チラシ限定】【さいたま市限定】【市内最安値】
青系、水色系、緑系、紫系
一応自分で簡単に作成しました内容を参考にしてください
(金額・プラン項目当)

はるきち様

今回は素敵なご提案本当にありがとうございます。
弊社女性スタッフの推薦が1番多かったです。
後ほど多少の修正依頼をお願いしたいと思います。

引き続き宜しくお願い致します。

今回は皆さまとても素敵なご提案ありがとうございました。

皆さまそれぞれ良い所があり中々決められずにギリギリになってしまい申し訳ありませんでした。

コロナが落ち着きましたら、通常プランでのチラシも考えておりますので
また宜しくお願いしたいと思います。

今回は本当にありがとうございました。

```html
<!DOCTYPE html>
<html lang="ja">
<head>
<meta charset="utf-8">
<title>アオイ葬祭 シンプル火葬式プラン</title>
<link href="https://fonts.googleapis.com/css2?family=Noto+Sans+JP:wght@400;500;700;900&family=Noto+Serif+JP:wght@500;700;900&display=swap" rel="stylesheet">
<style>
:root{
  --navy:#1e2c66;
  --navy-2:#2f3f80;
  --sky:#e3eaf5;
  --mist:#eef2f8;
  --line:#b9c5dc;
  --green:#2f8a3c;
  --text:#28304a;
  --white:#ffffff;
}
*{box-sizing:border-box;margin:0;padding:0}
html,body{width:846px;height:1200px;overflow:hidden;background:var(--white)}
body{font-family:"Noto Sans JP",sans-serif;color:var(--text)}
.flyer{position:relative;width:846px;height:1200px;overflow:hidden;background:linear-gradient(180deg,#f7f8fb 0%,#ffffff 55%)}
.abs{position:absolute}

/* hero */
.hero-photo{left:0;top:0;width:450px;height:660px;background:radial-gradient(ellipse at 35% 40%,#ffffff 0%,#e6ebf3 40%,#c9d3e4 70%,rgba(255,255,255,0) 100%)}
.hero-band{left:0;top:270px;width:470px;height:190px;background:linear-gradient(100deg,rgba(30,44,102,.85) 0%,rgba(47,63,128,.55) 70%,rgba(47,63,128,0) 100%)}
.hero-copy{left:30px;top:345px;color:var(--white);font-family:"Noto Serif JP",serif;font-size:20px;line-height:1.9;letter-spacing:.08em}

.badge{width:124px;height:124px;border-radius:50%;background:var(--white);border:2px solid var(--line);box-shadow:0 2px 6px rgba(30,44,102,.15);display:flex;align-items:center;justify-content:center;text-align:center;font-family:"Noto Serif JP",serif;font-weight:700;font-size:21px;line-height:1.3;color:var(--navy)}
.plan-title{left:430px;top:196px;width:380px;text-align:center;font-family:"Noto Serif JP",serif;font-size:26px;font-weight:700;letter-spacing:.12em;color:var(--navy)}
.plan-price{left:400px;top:232px;width:430px;text-align:center;font-family:"Noto Serif JP",serif;font-weight:900;color:var(--navy);font-size:66px;line-height:1.1}
.plan-price small{font-size:30px}

/* plan box */
.plan-box{left:422px;top:322px;width:400px;height:300px;background:rgba(255,255,255,.92);border:1px solid var(--line)}
.plan-head{margin:10px auto 8px;width:220px;background:var(--navy);color:var(--white);text-align:center;font-size:15px;font-weight:700;padding:4px 0;border-radius:14px}
.items{display:grid;grid-template-columns:repeat(4,1fr);gap:8px 8px;padding:0 12px}
.item{text-align:center;font-size:10.5px;line-height:1.3}
.item .pic{height:52px;background:linear-gradient(135deg,#d9dfe9,#aeb9cc);margin-bottom:3px}
.plan-note{font-size:11px;text-align:center;margin-top:8px;color:var(--text)}
.safety{display:flex;align-items:center;gap:8px;margin:8px 12px 0;border-top:1px dashed var(--line);padding-top:8px}
.safety-label{font-size:13px;font-weight:700;color:var(--green);line-height:1.3;width:110px}
.safety-icon{width:52px;text-align:center;font-size:10px}
.safety-icon svg{display:block;margin:0 auto 2px}

/* lower */
.aid{left:15px;top:645px;width:262px;height:430px;background:var(--sky);padding:14px 14px}
.aid-tag{display:inline-block;background:var(--navy);color:var(--white);font-size:12px;padding:3px 10px;border-radius:3px;margin-bottom:10px}
.aid h3{font-size:13px;color:var(--navy);margin:10px 0 4px}
.aid p{font-size:11.5px;line-height:1.7}
.aid-call{margin-top:18px;font-size:12px}
.tel-row{display:flex;align-items:center;gap:6px;font-weight:900;color:var(--navy)}
.tel-mark{background:var(--green);color:var(--white);font-size:11px;font-weight:700;padding:2px 5px;border-radius:3px}

.about{left:285px;top:645px;width:268px;height:430px;background:var(--white);border:1px solid var(--line);padding:26px 22px}
.about h2{font-family:"Noto Serif JP",serif;font-size:21px;line-height:1.5;color:var(--navy);margin-bottom:16px}
.about p{font-size:13px;line-height:33px;background:repeating-linear-gradient(180deg,transparent 0 32px,var(--line) 32px 33px)}

.flow{left:565px;top:645px;width:266px;height:430px}
.flow-head{background:var(--navy);color:var(--white);text-align:center;font-family:"Noto Serif JP",serif;font-weight:700;font-size:17px;padding:8px 0}
.flow-body{background:var(--mist);height:390px;padding:12px 20px;display:flex;flex-direction:column;align-items:center}
.step{width:100%;background:var(--white);border:1px solid var(--line);text-align:center;font-size:13px;padding:8px 0;color:var(--navy);font-weight:500}
.arrow{width:0;height:0;border-left:9px solid transparent;border-right:9px solid transparent;border-top:10px solid var(--navy-2);margin:5px 0}

/* footer */
.free{left:15px;top:1088px;width:112px;height:104px;background:var(--navy);color:var(--white);text-align:center;padding-top:10px}
.free .s{font-size:11px}
.free .b{font-size:28px;font-weight:900;line-height:1.3}
.brand{left:145px;top:1090px;width:190px}
.brand-tag{font-size:12px;color:var(--navy);white-space:nowrap}
.brand-name{display:flex;align-items:center;gap:8px;font-size:28px;font-weight:900;color:var(--navy);margin-top:4px;line-height:1.3}
.brand-name i{display:inline-block;width:20px;height:20px;border-radius:50%;background:var(--green)}
.brand-addr{font-size:11px;margin-top:6px;white-space:nowrap}
.brand-tel{left:338px;top:1130px;display:flex;align-items:center;gap:8px;font-size:34px;font-weight:900;color:var(--navy);white-space:nowrap;line-height:1.2}
.brand-tel .tel-mark{font-size:13px}
.staff{left:690px;top:1050px;width:140px;height:95px;background:linear-gradient(180deg,#eef2f8,#cfd8e8)}
.bubble{left:608px;top:1030px;width:90px;height:76px;border-radius:50%;background:var(--white);border:1px solid var(--line);font-size:10px;line-height:1.4;text-align:center;padding-top:14px;color:var(--navy)}
.open{left:650px;top:1150px;width:185px;font-size:10px;line-height:1.5;color:var(--navy)}
</style>
</head>
<body>
<div class="flyer">
  <div class="abs hero-photo" role="img" aria-label="白と青の紫陽花の花の写真"></div>
  <div class="abs hero-band"></div>
  <p class="abs hero-copy">とにかくシンプルに<br>ご予算を抑えたい方へ</p>

  <div class="abs badge" style="left:368px;top:42px">チラシ<br>限定</div>
  <div class="abs badge" style="left:510px;top:42px">さいたま<br>市民限定</div>
  <div class="abs badge" style="left:652px;top:42px">市内<br>最安値</div>

  <h1 class="abs plan-title">シンプル火葬式プラン</h1>
  <p class="abs plan-price">75,000円<small>(税別)</small></p>

  <section class="abs plan-box">
    <div class="plan-head">プランに含まれる項目</div>
    <div class="items">
      <div class="item"><div class="pic" role="img" aria-label="搬送車両の写真"></div>ご遺体搬送<br>(車両)</div>
      <div class="item"><div class="pic" role="img" aria-label="安置室の写真"></div>ご遺体保管<br>(安置料)</div>
      <div class="item"><div class="pic" role="img" aria-label="お棺の写真"></div>お棺一式</div>
      <div class="item"><div class="pic" role="img" aria-label="ドライアイスの写真"></div>ドライアイス</div>
      <div class="item"><div class="pic" role="img" aria-label="骨壺の写真"></div>骨壺・骨箱</div>
      <div class="item"><div class="pic" role="img" aria-label="役所手続き書類の写真"></div>役所手続き<br>代行</div>
      <div class="item"><div class="pic" role="img" aria-label="お花の写真"></div>お別れ花</div>
      <div class="item"><div class="pic" role="img" aria-label="スタッフの写真"></div>運営スタッフ</div>
    </div>
    <p class="plan-note">プラン内容以外：火葬料・待合室料・返礼品・ご飲食代・宗教費</p>
    <div class="safety">
      <p class="safety-label">感染症予防対策も<br>取り組んでいます</p>
      <div class="safety-icon"><svg width="28" height="28" viewBox="0 0 28 28"><circle cx="14" cy="14" r="13" fill="none" stroke="#1e2c66" stroke-width="2"/><rect x="12" y="6" width="4" height="12" rx="2" fill="#1e2c66"/><circle cx="14" cy="19" r="4" fill="#1e2c66"/></svg>検温実施</div>
      <div class="safety-icon"><svg width="28" height="28" viewBox="0 0 28 28"><circle cx="14" cy="14" r="13" fill="none" stroke="#1e2c66" stroke-width="2"/><path d="M9 9h2v10H9zM17 9h2v10h-2z" fill="#1e2c66"/><path d="M12 14h4" stroke="#1e2c66" stroke-width="2"/></svg>間隔確保</div>
      <div class="safety-icon"><svg width="28" height="28" viewBox="0 0 28 28"><circle cx="14" cy="14" r="13" fill="none" stroke="#1e2c66" stroke-width="2"/><rect x="10" y="11" width="8" height="10" rx="1" fill="#1e2c66"/><rect x="12" y="7" width="4" height="4" fill="#1e2c66"/></svg>除菌</div>
      <div class="safety-icon"><svg width="28" height="28" viewBox="0 0 28 28"><circle cx="14" cy="14" r="13" fill="none" stroke="#1e2c66" stroke-width="2"/><rect x="8" y="8" width="12" height="12" fill="none" stroke="#1e2c66" stroke-width="2"/></svg>飛沫ボード</div>
    </div>
  </section>

  <section class="abs aid">
    <span class="aid-tag">ご存知ですか？公的補助金</span>
    <h3>【国民健康保険の方】</h3>
    <p>故人が加入していた場合、申請により葬祭費として補助金が支給されます。</p>
    <h3>【社会保険の方】</h3>
    <p>埋葬料として一定額が支給されます。詳しくはお問い合わせください。</p>
    <h3>【手続き代行】</h3>
    <p>面倒な申請も当社スタッフがお手伝いいたします。</p>
    <div class="aid-call">まずはご相談ください
      <div class="tel-row"><span class="tel-mark">無料</span><span style="font-size:22px">0120-53-1046</span></div>
    </div>
  </section>

  <section class="abs about">
    <h2>火葬式って<br>どういうお葬式？</h2>
    <p>火葬式は通夜や告別式を行わず、ご家族やごく親しい方だけでお見送りをする形式です。費用と時間を抑え、密を避けて静かにお別れができます。</p>
  </section>

  <section class="abs flow">
    <div class="flow-head">火葬式の流れ</div>
    <div class="flow-body">
      <div class="step">ご連絡（24時間受付）</div><div class="arrow"></div>
      <div class="step">ご遺体搬送・ご安置</div><div class="arrow"></div>
      <div class="step">お打ち合わせ</div><div class="arrow"></div>
      <div class="step">ご納棺</div><div class="arrow"></div>
      <div class="step">火葬</div><div class="arrow"></div>
      <div class="step">収骨・解散</div>
    </div>
  </section>

  <div class="abs free">
    <p class="s">事前相談ご依頼</p>
    <p class="b">無料</p>
    <p class="s">365日24時間<br>いつでもOK</p>
  </div>

  <div class="abs brand">
    <p class="brand-tag">信頼・実績のある葬儀社</p>
    <p class="brand-name"><i></i>アオイ葬祭</p>
    <p class="brand-addr">さいたま市緑区上小池412-5</p>
  </div>
  <div class="abs brand-tel"><span class="tel-mark">無料</span>0120-53-1046</div>

  <div class="abs staff" role="img" aria-label="案内するスタッフのイラスト"></div>
  <div class="abs bubble">プランの詳細は<br>お気軽に<br>お問い合わせを</div>
  <p class="abs open">【24時間年中無休】<br>電話一本ですぐにお伺いいたします</p>
</div>
</body>
</html>
```